Bring Days 4 Wonder campaign: promoting kids play in the UK - Website Redesign

Bring Days 4 Wonder is a national UK campaign that promotes the value of play for children. The current website is live at http://www.bringdays4wonder.co.uk. This website has been live for 4 years and now needs to be redesigned. The target audience is parents of young children up to the age of 12.

The current site was designed with a series of old adverts in mind. Here is an example of an old advert: http://vidshare.example/k3RwqLmZ8Tb

Criticisms of existing site:
The design represented the adverts too closely. The result was a website that mirrors the adverts rather than complements them.
The color scheme is too dark.
Text-heavy pages (e.g. http://www.bringdays4wonder.co.uk/fun.php) are dull and not FUN!

New site
We have recently had a series of new video adverts produced:
advert 1: http://vidshare.example/Hq2vXnB7eJs
advert 2: http://vidshare.example/Wm9cTpR4uLd
advert 3: http://vidshare.example/Zg5sKbN1oVe

The new site should be cleaner and brighter than the existing site, possibly with a white background using graphics, fonts and advert characters (see attached character graphics files) to add the element of fun and play.

The homepage should include:
1. Bring Days for Wonder logo (attached)
2. Social Media links (visible on all pages of the site) – Facebook, Twitter, YouTube
3. Link to the BringDays4Wonder app page of the site (visible on all pages)
4. Image/video placeholder that the user can scroll through, view full-size images and play videos.
5. Text area to hold approximately 100 words describing the purpose of the campaign
6. Site footer to contain the same information as on the existing site along with the Northern Game & Craft Guild logo (attached)

Site structure:
One change to the site structure… the “Brought to you by” menu item will be removed from the top-level menu.

General:
Some pages on the existing site are quite text-heavy, we would like to break up text on these pages in some way. Graphical division of paragraphs, use of advert characters?

Please note that all attached graphics file are the property of the Northern Game & Craft Guild and must only be used for the purpose of this project.

```html
<!DOCTYPE html>
<html lang="en">
<head>
<meta charset="utf-8">
<title>Bring Days for Wonder</title>
<link href="https://fonts.googleapis.com/css2?family=Fredoka:wght@500;600&family=Open+Sans:wght@400&display=swap" rel="stylesheet">
<style>
  :root {
    --page: #ffffff;
    --ink: #4a4a4a;
    --nav: #9a9a9a;
    --title: #1fa9e1;
    --brand: #7a64ad;
    --rule: #8c8c8c;
    --player: #1b1b1b;
    --progress: #cc181e;
    --buffer: #5a5a5a;
    --active: #f5a623;
    --arrow: #c9c9c9;
  }
  * { box-sizing: border-box; margin: 0; padding: 0; }
  html, body { width: 1200px; height: 616px; overflow: hidden; background: var(--page); }
  body { position: relative; font-family: "Open Sans", Arial, sans-serif; color: var(--ink); }

  .edge { position: absolute; top: 0; height: 616px; }
  .edge--left { left: 162px; }
  .edge--right { left: 1124px; }

  .brand { position: absolute; left: 18px; top: 40px; width: 132px; display: flex; align-items: center; gap: 8px; }
  .brand__dot { width: 18px; height: 18px; border-radius: 50%; background: var(--brand); flex: none; }
  .brand__name { font-family: "Fredoka", sans-serif; font-weight: 600; font-size: 21px; line-height: 1.05; color: var(--brand); }

  .site-nav { position: absolute; left: 0; top: 162px; width: 147px; text-align: right; list-style: none; }
  .site-nav li { font-family: "Fredoka", sans-serif; font-weight: 600; font-size: 14.5px; color: var(--nav); height: 27.7px; }
  .site-nav .slash { font-weight: 500; margin-right: 4px; color: #b3b3b3; }

  .social { position: absolute; left: 24px; top: 450px; width: 115px; height: 26px; }
  .partner { position: absolute; left: 62px; top: 492px; width: 40px; height: 36px; border-radius: 6px; background: #d9d4e8; }
  .legal { position: absolute; left: 14px; top: 538px; width: 138px; text-align: center; font-size: 7.6px; line-height: 12.5px; color: #555; }
  .legal a { color: #555; }

  .player { position: absolute; left: 237px; top: 87px; width: 538px; height: 328px; background: var(--player); }
  .player__frame { position: absolute; left: 0; top: 0; width: 538px; height: 298px; background: linear-gradient(100deg, #c85a2c 0%, #8a4a2a 30%, #c99466 50%, #6a3a2a 68%, #d8c484 100%); }
  .player__track { position: absolute; left: 0; top: 298px; width: 538px; height: 4px; background: var(--buffer); }
  .player__played { position: absolute; left: 0; top: 0; width: 27px; height: 4px; background: var(--progress); }
  .player__buffer { position: absolute; left: 27px; top: 0; width: 46px; height: 4px; background: #8a8a8a; }
  .player__knob { position: absolute; left: 22px; top: -3px; width: 10px; height: 10px; border-radius: 50%; background: #eee; }
  .player__controls { position: absolute; left: 0; top: 302px; width: 538px; height: 26px; }
  .player__time { position: absolute; left: 76px; top: 308px; font-size: 9px; line-height: 14px; color: #ddd; font-family: Arial, sans-serif; }
  .player__time b { color: #fff; }

  .reel { position: absolute; left: 248px; top: 423px; width: 516px; height: 70px; }
  .reel__item { position: absolute; top: 0; width: 70px; height: 70px; }
  .reel__item--active { outline: 3px solid var(--active); outline-offset: -3px; }

  .intro { position: absolute; left: 792px; top: 116px; width: 259px; }
  .intro__title { font-family: "Fredoka", sans-serif; font-weight: 600; font-size: 22.5px; color: var(--title); margin-bottom: 4px; }
  .intro__body { font-size: 11.3px; line-height: 17.35px; color: var(--ink); }

  .crew { position: absolute; }
  .crew--top { left: 984px; top: 9px; width: 143px; height: 57px; background: linear-gradient(90deg, #4bb36a, #f2c94c, #2f4fa3, #e85a5a); border-radius: 6px; opacity: .55; }
  .crew--bottom { left: 168px; top: 544px; width: 232px; height: 58px; background: linear-gradient(90deg, #3aa7d9, #f6c445, #e86aa0, #e8623a, #f6b93b); border-radius: 6px; opacity: .55; }
  .crew--corner { left: 1130px; top: 546px; width: 70px; height: 56px; background: linear-gradient(90deg, #3aa7d9, #f6c445); border-radius: 6px 0 0 6px; opacity: .55; }
</style>
</head>
<body>

<svg class="edge edge--left" width="6" height="616" viewBox="0 0 6 616" aria-hidden="true">
  <path d="M3 0 C1 80 5 160 3 240 S1 400 4 480 S2 580 3 616" fill="none" stroke="var(--rule)" stroke-width="1"/>
</svg>
<svg class="edge edge--right" width="6" height="616" viewBox="0 0 6 616" aria-hidden="true">
  <path d="M3 0 C5 90 1 170 3 260 S5 420 2 500 S4 580 3 616" fill="none" stroke="var(--rule)" stroke-width="1"/>
</svg>

<header class="brand">
  <span class="brand__dot"></span>
  <span class="brand__name">Bring Days for Wonder</span>
</header>

<ul class="site-nav">
  <li><span class="slash">//</span>Play Right Now</li>
  <li><span class="slash">//</span>Get Involved</li>
  <li><span class="slash">//</span>Why Pltay</li>
  <li><span class="slash">//</span>Fun Forever</li>
  <li><span class="slash">//</span>Resources</li>
</ul>

<svg class="social" viewBox="0 0 115 26" aria-label="Social media and app links">
  <polygon points="0,0 115,0 109,13 115,26 0,26 6,13" fill="var(--brand)"/>
  <circle cx="28" cy="13" r="8" fill="#fff"/>
  <circle cx="49" cy="13" r="8" fill="#fff"/>
  <circle cx="70" cy="13" r="8" fill="#fff"/>
  <rect x="86" y="4" width="10" height="17" rx="2" fill="none" stroke="#fff" stroke-width="1.6"/>
  <rect x="89" y="18" width="4" height="1.4" fill="#fff"/>
</svg>

<div class="partner" role="img" aria-label="Partner badge"></div>

<footer class="legal">
  ©2014 Northern Game &amp; Craft<br>
  Guild Ltd.<br>
  14 Millbrook Lane, Leeds,<br>
  LS9 4QT // <a href="#">Disclaimer</a>
</footer>

<section class="player">
  <div class="player__frame" role="img" aria-label="Video still of campaign presenter speaking to camera"></div>
  <div class="player__track">
    <div class="player__played"></div>
    <div class="player__buffer"></div>
    <div class="player__knob"></div>
  </div>
  <svg class="player__controls" viewBox="0 0 538 26" aria-hidden="true">
    <polygon points="19,7 19,19 30,13" fill="#bbb"/>
    <polygon points="50,10 54,10 59,6 59,20 54,16 50,16" fill="#bbb"/>
    <path d="M62 9 q3 4 0 8" stroke="#bbb" stroke-width="1.3" fill="none"/>
    <circle cx="424" cy="13" r="4.5" fill="#bbb"/>
    <rect x="444" y="9" width="11" height="8" fill="#bbb"/>
    <circle cx="475" cy="13" r="4.5" fill="none" stroke="#bbb" stroke-width="2.5"/>
    <rect x="494" y="8" width="14" height="10" fill="none" stroke="#bbb" stroke-width="1.6"/>
    <path d="M517 7 h4 M517 7 v4 M532 7 h-4 M532 7 v4 M517 19 h4 M517 19 v-4 M532 19 h-4 M532 19 v-4" stroke="#bbb" stroke-width="1.6"/>
  </svg>
  <div class="player__time"><b>0:06</b> / 3:00</div>
</section>

<section class="reel">
  <svg style="position:absolute;left:2px;top:22px" width="18" height="26" viewBox="0 0 18 26" aria-label="Previous">
    <path d="M16 2 L4 13 L16 24" fill="none" stroke="var(--arrow)" stroke-width="4"/>
  </svg>
  <div class="reel__item reel__item--active" style="left:29px;background:linear-gradient(160deg,#6a3a22,#c98a5c)" role="img" aria-label="Thumbnail: presenter video"></div>
  <div class="reel__item" style="left:107px;background:linear-gradient(160deg,#9ccf7a,#e6b36a)" role="img" aria-label="Thumbnail: children exploring illustration"></div>
  <div class="reel__item" style="left:185px;background:linear-gradient(160deg,#6f8fc4,#e58fb0)" role="img" aria-label="Thumbnail: learn to share illustration"></div>
  <div class="reel__item" style="left:263px;background:linear-gradient(160deg,#e9c79a,#b8d8e0)" role="img" aria-label="Thumbnail: imagine illustration"></div>
  <div class="reel__item" style="left:341px;background:linear-gradient(160deg,#8a5a48,#e0b59a)" role="img" aria-label="Thumbnail: presenter interview"></div>
  <div class="reel__item" style="left:419px;background:linear-gradient(160deg,#d8d0c0,#c4b24a)" role="img" aria-label="Thumbnail: children playing with a box"></div>
  <svg style="position:absolute;left:496px;top:22px" width="18" height="26" viewBox="0 0 18 26" aria-label="Next">
    <path d="M2 2 L14 13 L2 24" fill="none" stroke="var(--arrow)" stroke-width="4"/>
  </svg>
</section>

<article class="intro">
  <h1 class="intro__title">Title Goes Here</h1>
  <p class="intro__body">Lorem ipsum dolor sit amet, consectetur adipiscing elit. Nulla mollis venenatis augue, vitae hendrerit lectus tempor ac. Donec fermentum nibh lacus. Proin urna mauris, consectetur vel ligula quis, interdum ullamcorper lacus. Quisque hendrerit scelerisque gravida. Cum sociis natoque penatibus et magnis dis parturient montes, nascetur ridiculus mus. Aenean placerat luctus consequat. Suspendisse porttitor leo non sapien ultricies suscipit. Ut pulvinar suscipit dui, a feugiat dolor condimentum a. Ut vel purus aliquam, consectetur lacus sed, tristique iis natoque penatibus et mag diam. Proin viverra arcu eget mollis rutrum. Vestibulum ante ipsum primis in faucibus orci luctus et ultrices posuere cubilia turae.</p>
</article>

<div class="crew crew--top" role="img" aria-label="Illustrated children holding hands"></div>
<div class="crew crew--bottom" role="img" aria-label="Illustrated children holding hands in a row"></div>
<div class="crew crew--corner" role="img" aria-label="Illustrated children holding hands, continuing off the page"></div>

</body>
</html>
```